TOR Capital Allies LLC a High Risk Big Rewards company for Rich Young Entrepreneurs

We would like a very modern, powerful in the eyes of our customers, modern, minimalist feel, financial gain. this business card is for young Rich entrepreneurs who want to invest money into High Risk, Big Rewards Businesses. The card Should sell the business!! let your creativity go Wild! I pick most of the designers for this project because of your BOLD Designs, I would like this card to be Bold, Modern, Minimalist, use as many effects in your graphic Artist Mind, Do not let the Financial sound of this business to make you think Conservative that's the last thing we are! if you have a lot of money and you want to play a risky market call US
Updates

Project Deadline Extended
Reason: have not received, enough designs to choose 1st and second place, sure I have received over 100 designs but it seems most designers are submitting every card they have ever made before and calling it mine, please we are looking for fresh ideas please!

Target Market(s)

Private Risky Investors

Industry/Entity Type

Financial

Contact Information for Business Card

powerful in the eyes of our customers,modern, minimalist feel

Font styles to use
Other font styles liked:
• Modern feeling fonts

Requirements
Must have
• The Company Name is TOR Capital Allies LLC and it must be on the CARD
• My Name, title, Cell , email
• Dalton Fairweather G.E.D.
• Managing Member
• 404.658.1937
• dalton@torcapitalallies.example
Nice to have
• try a black thick plastic card with round corners with Dalton Fairweather GED (make sure GED is smaller than name) just on one side of the card, and my phone number with out the icons and email on the other side, this card should look like a exclusive credit card or exclusive VIP card, something you would never loose

```html
<!DOCTYPE html>
<html lang="en">
<head>
<meta charset="utf-8">
<title>TOR Capital Allies LLC – Business Card</title>
<link rel="stylesheet" href="https://fonts.googleapis.com/css2?family=Crimson+Text:wght@400;600&display=swap">
<style>
  :root {
    --page-bg: #e6e6e6;
    --brand-blue: #0788fb;
    --band-black: #141414;
    --card-light: #ebebeb;
    --card-light-edge: #dcdcdc;
    --mark-silver: #d6d6d6;
    --mark-white: #f4f4f4;
    --ink: #1e1e1e;
  }
  html, body {
    margin: 0;
    padding: 0;
    width: 1200px;
    height: 1000px;
    overflow: hidden;
    background: var(--page-bg);
  }
  .sheet { display: block; width: 1200px; height: 1000px; }
  .serif { font-family: "Crimson Text", Georgia, serif; }
  .front-band-blue { fill: var(--brand-blue); }
  .front-band-black { fill: var(--band-black); }
  .front-name { fill: var(--mark-silver); }
  .back-face { fill: url(#backShade); }
  .back-stripe { fill: var(--brand-blue); }
  .back-name { fill: var(--mark-white); }
  .holder-name { fill: var(--ink); font-weight: 600; font-variant: small-caps; }
  .holder-detail { fill: var(--ink); font-weight: 400; }
</style>
</head>
<body>
<svg class="sheet" viewBox="0 0 1200 1000" xmlns="http://www.w3.org/2000/svg">
  <defs>
    <radialGradient id="backShade" cx="0.5" cy="0.5" r="0.75">
      <stop offset="0" stop-color="#f1f1f1"/>
      <stop offset="1" stop-color="#dedede"/>
    </radialGradient>
    <clipPath id="backClip">
      <rect x="205" y="500" width="797" height="442"/>
    </clipPath>
  </defs>

  <!-- Front of card -->
  <g class="card-front">
    <rect class="front-band-blue" x="205" y="42" width="797" height="139"/>
    <rect class="front-band-black" x="205" y="181" width="797" height="193"/>
    <rect class="front-band-blue" x="205" y="374" width="797" height="112"/>
    <text class="serif front-name" x="600" y="280" text-anchor="middle" font-size="62" letter-spacing="10">TOR</text>
    <text class="serif front-name" x="600" y="313" text-anchor="middle" font-size="24" style="font-variant: small-caps">Capital Allies LLC</text>
  </g>

  <!-- Back of card -->
  <g class="card-back" clip-path="url(#backClip)">
    <rect class="back-face" x="205" y="500" width="797" height="442"/>
    <polygon class="back-stripe" points="515,500 790,500 347,942 205,942 205,808"/>
    <polygon class="back-stripe" points="1002,838 1002,942 898,942"/>

    <g class="serif">
      <text class="back-name" x="352" y="778" font-size="76" letter-spacing="10" transform="rotate(-45 352 778)">TOR</text>
      <text class="back-name" x="372" y="862" font-size="30" transform="rotate(-45 372 862)" style="font-variant: small-caps">Capital Allies LLC</text>

      <text class="holder-name" x="510" y="883" font-size="27" transform="rotate(-45 510 883)">Dalton Fairweather <tspan font-size="22">G.E.D.</tspan></text>
      <text class="holder-detail" x="546" y="888" font-size="22" transform="rotate(-45 546 888)">Managing Member</text>
      <text class="holder-detail" x="643" y="884" font-size="22" transform="rotate(-45 643 884)">404.658.1937</text>
      <text class="holder-detail" x="713" y="887" font-size="21" transform="rotate(-45 713 887)">dalton@torcapitalallies.example</text>
    </g>
  </g>
</svg>
</body>
</html>
```